Passport Brochure

We are a start-up training and staffing company called Vellor Advisory. We assist people in getting work in the Financial Industry.
We need a brochure for our new "Learner Waypoint Scheme".
We've put together a mock up of what we are looking for but we need someone to put a more professional touch on it, see "Creative Brief" attached obviously the pictures are just examples to give an idea.
The 4 slides will be printed with each slide being 3.5 x 5 inches gloss brochure.
We want the front page to have the picture shown or very similar.
The middle of the brochure should look like the center-fold of a passport slide 2 should be the left page of a passport and slide 3 would be the right side of a passport and have an approved symbol
Slide 3 should have an integrated picture of the Marrowgate Tower
The back should look like the back of a passport and contain our logo, attached.

Hello and Thank you all for your great designs. Can everyone please ensure that all pages(front and back) within each design are added to the same submission. Thanks, Corwin

```html
<!DOCTYPE html>
<html lang="en">
<head>
<meta charset="utf-8">
<title>Learner Waypoint Scheme – Salary Page</title>
<link href="https://fonts.googleapis.com/css2?family=Tinos:wght@400;700&display=swap" rel="stylesheet">
<style>
  :root {
    --paper: #fdd99a;
    --paper-deep: #f9cf88;
    --ink: #862b4f;
  }
  * { margin: 0; padding: 0; box-sizing: border-box; }
  html, body { width: 840px; height: 1200px; overflow: hidden; }
  body {
    background: var(--paper);
    font-family: "Tinos", "Times New Roman", serif;
    color: var(--ink);
  }
  .page {
    position: relative;
    width: 840px;
    height: 1200px;
    background: radial-gradient(circle at 50% 40%, var(--paper) 0%, var(--paper-deep) 100%);
  }
  .page-tab {
    position: absolute;
    left: 30px;
    top: 0;
    width: 118px;
    height: 228px;
    background: var(--ink);
    border-radius: 0 0 59px 59px;
  }
  .salary-heading {
    position: absolute;
    left: 160px;
    top: 98px;
    font-weight: 700;
    line-height: 1;
  }
  .salary-heading .kicker {
    display: block;
    font-size: 39px;
    letter-spacing: 0.5px;
  }
  .salary-heading .figure {
    display: block;
    font-size: 61px;
    margin-top: 2px;
  }
  .tagline {
    position: absolute;
    left: 0;
    width: 840px;
    top: 254px;
    text-align: center;
    font-size: 29px;
    font-weight: 700;
  }
  .learning-box {
    position: absolute;
    left: 24px;
    top: 317px;
    width: 789px;
    height: 848px;
    border: 3px solid var(--ink);
    border-radius: 32px;
    padding: 36px 24px 0 26px;
  }
  .learning-title {
    font-size: 22px;
    font-weight: 700;
    margin-bottom: 4px;
  }
  .learning-list {
    list-style: none;
    font-size: 22px;
    line-height: 32px;
    text-align: justify;
  }
  .learning-list li { margin-bottom: 4px; }
  .approved-stamp {
    position: absolute;
    left: 560px;
    top: 680px;
    width: 140px;
    height: 140px;
    border-radius: 50%;
    background: radial-gradient(circle, rgba(134,43,79,0.85) 0%, rgba(134,43,79,0.55) 70%, rgba(134,43,79,0.2) 100%);
  }
</style>
</head>
<body>
  <main class="page">
    <div class="page-tab"></div>

    <h1 class="salary-heading">
      <span class="kicker">AVERAGE STARTING</span>
      <span class="figure">SALARY- £35,000</span>
    </h1>

    <h2 class="tagline">LETS GET YOU ON YOUR WAY</h2>

    <section class="learning-box">
      <h3 class="learning-title">What you can expect to learn;</h3>
      <ul class="learning-list">
        <li>– Everything you need to know to work in Finance.</li>
        <li>– The history of Banking and Finance.</li>
        <li>– Finance Fundamentals - Macro Economics and The Big Picture.</li>
        <li>– Corporate Investment Banking - M&amp;A, IPOs, LBO.</li>
        <li>– Capital Markets and the various Assets Classes - Fixed Income Equity etc.</li>
        <li>– Financial Instruments - Bonds, Stocks etc.</li>
        <li>– Derivatives Overview - CDS, CDOs, Futures, Options, Swaps etc.</li>
        <li>– Financial Players - Banks, Buy Side firms, Brokers etc.</li>
        <li>– Markets and Exchanges - How they work, how people make money.</li>
        <li>– Banking Terminology - All the buss words and financial terms needed.</li>
        <li>– Business Etiquette - Not taught but extremely important to a successful career.</li>
        <li>– Fully Financial / Banking Crisis discussion and explanation.</li>
      </ul>
      <div class="approved-stamp" role="img" aria-label="Approved passport rubber stamp"></div>
    </section>
  </main>
</body>
</html>
```